Corporate Brochure for Exclusive Consultant Firm

Brochure needed for insurance adjusting firm. Our company is highly specialized in our field. Our target market are executives at insurance companies, insurance risk managers and insurance brokers. We specialize in industrial insurance claims in the mining, forestry, chemical plants, construction and legal liability sectors.

We are looking for a 8 1/2 x 11 bi-fold brochure that tells the story of our company. Our corporate colors are used. There is a place at the back for the pictures and short bios of the 3 people on our web site.

Refer to our web site for full details on our company. Please do not do cut and paste, we are looking for a creative, clean, professional design.

We want a brochure that we can send to the printer, so the necessary files for that. Also, we want the brochure to be in electronic form so we can distribute the brochure electronically.

www.halvorenclaims.example

Target Market(s)

Corporate executives

Industry/Entity Type

Insurance

Requirements
Must have
• clean, professional, modern look reflecting our website. Pictures of the 3 persons, short bio of each near the back. Can use photos from the site or use other files. Must provide files for print, and produce a digital version that we can share with clients electronically.
Nice to have
• COLORS: orange, light grey, white, black (to be used minimally, more as accent)
Should not have
• exact cut and paste from our website. We are looking for a clean modern and new brochure to market our business .

```html
<!DOCTYPE html>
<html lang="en">
<head>
<meta charset="utf-8">
<title>Halvoren Claims – Bi-fold Brochure</title>
<link href="https://fonts.googleapis.com/css2?family=Open+Sans:wght@400;600;700&family=Montserrat:wght@600;700;800&display=swap" rel="stylesheet">
<style>
:root{
  --orange:#f58a1f;
  --charcoal:#333335;
  --grey:#e6e6e6;
  --ink:#3d3d3d;
  --white:#ffffff;
}
*{box-sizing:border-box;margin:0;padding:0}
html,body{width:835px;height:1200px;overflow:hidden;background:var(--white);font-family:"Open Sans",Arial,sans-serif;color:var(--ink)}
.spread{position:absolute;left:38px;width:760px;height:555px;background:var(--white);box-shadow:0 0 0 1px #dcdcdc}
.spread--outside{top:20px}
.spread--inside{top:620px}
.panel{position:absolute;top:0;height:100%;overflow:hidden}

/* outside spread */
.team{left:0;width:380px}
.bio{position:absolute;left:24px;width:336px;height:130px;display:flex;gap:10px}
.bio__photo{width:58px;height:70px;flex:none;background:linear-gradient(160deg,#9a9a9a,#5a5a5a)}
.bio__text{width:150px;font-size:6.6px;line-height:1.5}
.bio__text strong{color:var(--charcoal)}
.bio__contact{width:118px;font-size:6.4px;line-height:1.7;padding-top:4px}
.bio__contact span{display:block}
.bio__contact span::before{content:"";display:inline-block;width:4px;height:4px;background:var(--orange);margin-right:4px;vertical-align:1px}
.team__footer{position:absolute;left:0;bottom:0;width:100%;height:74px;background:var(--charcoal);color:#cfcfcf;text-align:center;padding-top:12px}
.brand{display:inline-flex;align-items:center;gap:6px;font-family:"Montserrat",Arial,sans-serif;font-weight:800;letter-spacing:.08em;text-transform:uppercase;color:var(--orange)}
.brand__mark{width:10px;height:10px;background:var(--orange)}
.team__footer .brand{font-size:11px}
.team__footer p{font-size:6px;margin-top:8px;line-height:1.6}

.cover{left:380px;width:380px}
.cover__map{position:absolute;top:0;left:0;width:100%;height:150px;background:linear-gradient(135deg,#5b5b5e,#3a3a3c 60%,#2d2d2f)}
.cover .brand{position:absolute;top:32px;right:28px;font-size:14px}
.cover__photo{position:absolute;top:150px;left:0;width:100%;height:210px;background:linear-gradient(180deg,#2b2118 0%,#6b3b12 45%,#e08a2a 75%,#3a2614 100%)}
.cover__copy{position:absolute;top:378px;right:26px;width:210px;font-size:6.6px;line-height:1.55}
.cover__copy h2{font-family:"Montserrat",Arial,sans-serif;font-size:8px;font-weight:700;color:var(--charcoal);margin-bottom:6px;text-transform:uppercase;line-height:1.35}
.cover__bar{position:absolute;bottom:0;left:0;width:100%;height:40px;background:var(--charcoal);border-top:4px solid var(--orange);display:flex;align-items:center;justify-content:flex-end;padding-right:26px}
.site{font-family:"Montserrat",Arial,sans-serif;font-size:8px;font-weight:700;letter-spacing:.06em;color:var(--white);text-transform:uppercase}

/* inside spread */
.services{left:0;width:252px;padding:22px 18px 0 22px}
.topic{margin-bottom:9px}
.topic h3{font-family:"Montserrat",Arial,sans-serif;font-size:7.6px;font-weight:700;color:var(--orange);margin-bottom:2px}
.topic p{font-size:5.8px;line-height:1.5}
.collage{left:262px;width:230px;top:14px;height:527px;background:linear-gradient(180deg,#c9a27a 0%,#8c8f88 35%,#6f7a84 65%,#d98a3a 100%)}
.sectors{left:502px;width:258px;background:var(--grey);padding:34px 22px 0 24px}
.sectors .brand{font-size:12px;margin-bottom:18px}
.sectors p{font-size:6.2px;line-height:1.55}
.sector-list{list-style:none;margin:16px 0 16px}
.sector-list li{font-family:"Montserrat",Arial,sans-serif;font-size:10px;font-weight:700;color:var(--charcoal);margin-bottom:9px;display:flex;align-items:center;gap:8px}
.sector-list li::before{content:"";width:6px;height:6px;background:var(--orange);flex:none}
.sectors__bar{position:absolute;left:0;bottom:0;width:100%;height:34px;background:var(--charcoal);border-top:4px solid var(--orange);display:flex;align-items:center;justify-content:center}
</style>
</head>
<body>

<section class="spread spread--outside">
  <div class="panel team">
    <article class="bio" style="top:26px">
      <div class="bio__photo" role="img" aria-label="Portrait photo of Marcus Delaine"></div>
      <div class="bio__text"><strong>Marcus Delaine</strong> has been actively managing and adjusting large industrial claims for over twenty years. He has provided consulting services to insurers and brokers across energy and resource markets and holds a chartered designation.</div>
      <div class="bio__contact"><span>Founder &amp; Senior Adjuster</span><span>marcus@halvorenclaims.example</span><span>T (555) 014-2210</span><span>C (555) 014-2211</span></div>
    </article>
    <article class="bio" style="top:160px">
      <div class="bio__photo" role="img" aria-label="Portrait photo of Curtis Vanholt"></div>
      <div class="bio__text"><strong>Curtis Vanholt</strong> is a graduate of engineering and worked in heavy industry before joining the firm. He brings hands-on technical knowledge to complex losses in chemical and mining operations and leads our loss control work.</div>
      <div class="bio__contact"><span>Partner, Technical Claims</span><span>curtis@halvorenclaims.example</span><span>T (555) 014-2230</span><span>C (555) 014-2231</span></div>
    </article>
    <article class="bio" style="top:294px">
      <div class="bio__photo" role="img" aria-label="Portrait photo of Janet Orsova"></div>
      <div class="bio__text"><strong>Janet Orsova</strong> joined the firm with a background in forestry and commercial property claims. She is a member of the national adjusters association and oversees litigation support and client reporting files.</div>
      <div class="bio__contact"><span>Senior Claims Adjuster</span><span>janet@halvorenclaims.example</span><span>T (555) 014-2250</span><span>C (555) 014-2251</span></div>
    </article>
    <footer class="team__footer">
      <div class="brand"><span class="brand__mark"></span>Halvoren Claims</div>
      <p>1200 Ridgeway Avenue, Suite 400, Northbridge &nbsp;|&nbsp; T (555) 014-2200 &nbsp;|&nbsp; F (555) 014-2299<br>info@halvorenclaims.example &nbsp;|&nbsp; www.halvorenclaims.example</p>
    </footer>
  </div>

  <div class="panel cover">
    <div class="cover__map" role="img" aria-label="Dark grey world map backdrop"></div>
    <div class="brand"><span class="brand__mark"></span>Halvoren Claims</div>
    <div class="cover__photo" role="img" aria-label="Industrial refinery lit up at night"></div>
    <div class="cover__copy">
      <h2>Technical expertise for<br>specialty insurance markets</h2>
      <p>Halvoren Claims is a firm of highly skilled claims management and loss adjustment professionals. We specialize in managing and resolving large complex losses for insurers, brokers and risk managers in energy, mining, forestry, chemical and legal liability sectors.</p>
    </div>
    <div class="cover__bar"><span class="site">www.halvorenclaims.example</span></div>
  </div>
</section>

<section class="spread spread--inside">
  <div class="panel services">
    <div class="topic"><h3>Our Approach</h3><p>We deliver independent, timely and accurate adjusting services built on technical knowledge and a clear understanding of our clients' priorities.</p></div>
    <div class="topic"><h3>Experience</h3><p>Our team brings decades of field experience in complex industrial losses, with a record of fair and efficient outcomes on major claims.</p></div>
    <div class="topic"><h3>The Difference</h3><p>We combine adjusting expertise with engineering insight, allowing us to identify causes, quantify damage and guide recovery with confidence.</p></div>
    <div class="topic"><h3>Niche Expertise</h3><p>Our focus on specialty industrial risks means we understand the operations, equipment and exposures behind every claim we handle.</p></div>
    <div class="topic"><h3>Loss Control</h3><p>We help clients reduce future losses through site reviews, risk recommendations and practical advice drawn from real claims.</p></div>
    <div class="topic"><h3>Customer Service Tailored to Your Needs</h3><p>Every assignment is managed to your reporting standards, with direct access to senior adjusters from first notice to final settlement.</p></div>
    <div class="topic"><h3>Unmatched Success</h3><p>Our clients return to us for consistent results, clear communication and resolution of claims others find too complex.</p></div>
  </div>

  <div class="panel collage" role="img" aria-label="Photo collage of industry sites: refinery, forest, mine site, chemical plant, heavy equipment and construction"></div>

  <div class="panel sectors">
    <div class="brand"><span class="brand__mark"></span>Halvoren Claims</div>
    <p>Halvoren Claims is built to be a partner you can rely on, with a practical, hands-on approach to every loss. Our specialized services include:</p>
    <ul class="sector-list">
      <li>Energy</li>
      <li>Chemical Operations</li>
      <li>Forest Industry</li>
      <li>Mining</li>
      <li>Commercial Claims</li>
      <li>Litigation Support Services</li>
    </ul>
    <p>We are distinguished by our focus on providing our clients with an objective and thorough approach to claim handling, backed by technical depth and responsive service at every step of the process.</p>
    <div class="sectors__bar"><span class="site">www.halvorenclaims.example</span></div>
  </div>
</section>

</body>
</html>
```